COMPANY SIGN

I am in the process of ordering new company For Sale signs and stationary (business cards, envelopes, letterheads, and labels). I need a new design with my existing company logo. The TWO MOST IMPORTANT PROJECTS I need right now is the new design for the company sign and business cards. I've uploaded a .jpg file of my company logo.

I like the design to be eye catching and the background color of the company sign to be soothing to the eyes. Perhaps, using one of the color on the leaves of the logo or any other color that the designer think will go well with the logo. My favorite colors are teal or light olive color but don't let that affect your creativity.

Industry/Entity Type

Business

Requirements
Should not have
• Please don't use "Times New Roman" fonts or fonts that is hard to read.

```html
<!DOCTYPE html>
<html lang="en">
<head>
<meta charset="utf-8">
<title>Cedarline Realty Group – Business Card</title>
<link rel="stylesheet" href="https://fonts.googleapis.com/css2?family=Source+Sans+3:ital,wght@0,400;0,600;0,700;1,400&display=swap">
<style>
  :root {
    --sky: #c9deed;
    --band-light: #eef2be;
    --band-mid: #d3df86;
    --band-dark: #b4c548;
    --bark: #5b4331;
    --bark-text: #5a4330;
    --leaf: #9db83a;
    --paper: #ffffff;
  }
  * { margin: 0; padding: 0; box-sizing: border-box; }
  html, body {
    width: 1200px;
    height: 681px;
    overflow: hidden;
    background: var(--paper);
  }
  .card {
    position: relative;
    width: 1200px;
    height: 681px;
    font-family: "Source Sans 3", "Myriad Pro", sans-serif;
    overflow: hidden;
  }
  .card__sky {
    position: absolute;
    inset: 0 0 auto 0;
    height: 417px;
    background: var(--sky);
  }
  .brand {
    position: absolute;
    left: 0;
    right: 0;
    top: 232px;
    display: flex;
    justify-content: center;
    align-items: center;
    gap: 22px;
  }
  .brand__dot {
    width: 48px;
    height: 48px;
    border-radius: 50%;
    background: var(--leaf);
  }
  .brand__name {
    font-size: 80px;
    font-weight: 600;
    color: var(--bark-text);
    letter-spacing: 0.5px;
    line-height: 1;
  }
  .tagline-band {
    position: absolute;
    left: 0;
    right: 0;
    top: 417px;
    height: 62px;
    background: linear-gradient(to bottom, var(--band-light) 0%, var(--band-mid) 45%, var(--band-dark) 100%);
    display: flex;
    justify-content: center;
    align-items: center;
  }
  .tagline {
    font-size: 42px;
    color: var(--bark-text);
    font-weight: 400;
    line-height: 1;
  }
  .tagline em { font-style: italic; }
  .tagline strong { font-weight: 700; }
  .card__base {
    position: absolute;
    left: 0;
    right: 0;
    top: 479px;
    bottom: 0;
    background: var(--bark);
    color: var(--paper);
  }
  .agent {
    position: absolute;
    left: 54px;
    top: 34px;
  }
  .agent__name {
    font-size: 62px;
    font-weight: 700;
    line-height: 1;
  }
  .agent__title {
    font-size: 34px;
    font-style: italic;
    margin-top: 4px;
    line-height: 1;
  }
  .contact {
    position: absolute;
    right: 80px;
    top: 36px;
    text-align: right;
    font-size: 33px;
    line-height: 32px;
    font-style: normal;
  }
</style>
</head>
<body>
  <div class="card">
    <div class="card__sky">
      <div class="brand">
        <span class="brand__dot"></span>
        <span class="brand__name">Cedarline Realty Group</span>
      </div>
    </div>
    <div class="tagline-band">
      <p class="tagline">Your <em>Trusted</em> <strong>Property Partner Nearby</strong></p>
    </div>
    <div class="card__base">
      <div class="agent">
        <p class="agent__name">Dana Whitfield</p>
        <p class="agent__title">Realtor</p>
      </div>
      <address class="contact">
        1480 Linden Avenue #310<br>
        Oak Valley, CA 91720<br>
        Office: (555) 014-2870
      </address>
    </div>
  </div>
</body>
</html>
```